Business Card and Stationery for Bellwick Home Services
Bellwick Home Services
Professional
R. Owen Tallis
President/CEO
4187 Marrow Creek Lane,
Suite K
Baton Rouge LA 70342
rowentallis@bellwickhomeservices.biz
www.bellwickhomeservice.biz
Commercial License # 53419 Residential LIcense # 21398
The color formula for the orange is:
C=0 M=74 Y=100 K=0
We take care of all of your home needs.
Plumbing, Heating and AIr, Electrical, Remodeling, Roofing, New Construction, Insurance Damage Repairs, Fire Restoration, if its in you home, we can service it or take care of it for you!!!
THESE ARE JUST IDEAS, want to use the back for information, etc.......maybe a light watermark on the back, using part of the logo, showing under the lettering. Would like the back to be the orange color

```html
<!DOCTYPE html>
<html lang="en">
<head>
<meta charset="utf-8">
<title>Bellwick Home Services — Stationery Set</title>
<link href="https://fonts.googleapis.com/css2?family=Roboto+Slab:wght@700&family=Open+Sans:wght@400;600&display=swap" rel="stylesheet">
<style>
  :root {
    --orange: #f15a22;
    --orange-soft: #f7a37d;
    --paper: #ffffff;
    --ink: #4a4a4a;
    --ink-light: #8a8a8a;
    --flap: #5a5a5a;
    --rule: #b9b9b9;
    --ground: #eeeae4;
    --shadow: 0 2px 6px rgba(0,0,0,.18);
  }
  * { box-sizing: border-box; margin: 0; padding: 0; }
  html, body { width: 1200px; height: 446px; overflow: hidden; }
  body { background: var(--ground); font-family: "Open Sans", Arial, sans-serif; color: var(--ink); position: relative; }

  .sheet { position: absolute; background: var(--paper); box-shadow: var(--shadow); overflow: hidden; }

  /* brand lockup */
  .brand { display: flex; align-items: center; gap: 6px; }
  .brand-mark { background: var(--orange); border-radius: 4px; flex: none; }
  .brand-name { font-family: "Roboto Slab", Georgia, serif; font-weight: 700; color: var(--orange); line-height: 1.05; }

  .watermark {
    position: absolute; background: var(--orange); opacity: .07; border-radius: 22%;
  }

  /* business cards */
  .card { width: 125px; height: 72px; left: 19px; }
  .card-front { top: 180px; padding: 8px; }
  .card-front .brand-mark { width: 16px; height: 16px; }
  .card-front .brand-name { font-size: 7px; width: 60px; }
  .card-front .details { position: absolute; left: 8px; bottom: 10px; font-size: 3.6px; line-height: 1.5; color: var(--ink); }
  .card-front .band { position: absolute; left: 0; right: 0; bottom: 0; height: 4px; background: var(--orange); }
  .card-back { top: 271px; background: var(--orange); display: flex; align-items: center; justify-content: center; }
  .card-back .watermark { background: #fff; opacity: .14; width: 50px; height: 50px; left: 62px; top: 11px; }
  .card-back .brand-name { color: #fff; font-size: 8px; text-align: center; position: relative; }

  /* letterheads */
  .letterhead { width: 350px; height: 408px; top: 19px; }
  .lh-one { left: 163px; }
  .lh-two { left: 540px; }
  .letterhead .brand-mark { width: 34px; height: 34px; }
  .letterhead .brand-name { font-size: 13px; width: 110px; }
  .lh-one .brand { position: absolute; left: 24px; top: 20px; }
  .lh-one .contact { position: absolute; left: 150px; top: 22px; font-size: 5px; line-height: 1.55; color: var(--ink-light); }
  .lh-two .brand { position: absolute; left: 50%; transform: translateX(-50%); top: 20px; }
  .lh-one .watermark { width: 140px; height: 140px; left: 180px; top: 230px; }
  .lh-two .watermark { width: 120px; height: 120px; left: 115px; top: 140px; }
  .letterhead .footer { position: absolute; left: 0; right: 0; bottom: 0; }
  .letterhead .footer-rule { height: 2px; background: var(--rule); margin: 0 20px 3px; }
  .letterhead .footer-text { font-size: 4.6px; color: var(--ink-light); text-align: center; margin-bottom: 6px; }
  .letterhead .footer-band { height: 9px; background: var(--orange); }

  /* envelopes */
  .envelope-back { left: 907px; top: 19px; width: 270px; height: 245px; background: transparent; box-shadow: none; }
  .envelope-back svg { display: block; }
  .envelope-front { left: 804px; top: 269px; width: 377px; height: 140px; }
  .envelope-front .brand { position: absolute; left: 14px; top: 14px; }
  .envelope-front .brand-mark { width: 24px; height: 24px; }
  .envelope-front .brand-name { font-size: 10px; width: 84px; }
  .envelope-front .return { position: absolute; left: 14px; top: 44px; font-size: 4.6px; line-height: 1.5; color: var(--ink-light); }
  .envelope-front .watermark { width: 70px; height: 70px; right: 30px; top: 20px; }
  .envelope-front .band { position: absolute; left: 0; right: 0; bottom: 0; height: 6px; background: var(--orange); }
</style>
</head>
<body>

  <!-- Business card front -->
  <div class="sheet card card-front">
    <div class="brand">
      <span class="brand-mark"></span>
      <span class="brand-name">Bellwick Home Services</span>
    </div>
    <div class="details">
      <strong>R. Owen Tallis</strong>, President/CEO<br>
      4187 Marrow Creek Lane, Suite K, Baton Rouge LA 70342<br>
      rowentallis@bellwickhomeservices.biz<br>
      www.bellwickhomeservice.biz
    </div>
    <div class="band"></div>
  </div>

  <!-- Business card back -->
  <div class="sheet card card-back">
    <div class="watermark"></div>
    <span class="brand-name">Bellwick<br>Home Services</span>
  </div>

  <!-- Letterhead option 1 -->
  <div class="sheet letterhead lh-one">
    <div class="brand">
      <span class="brand-mark"></span>
      <span class="brand-name">Bellwick Home Services</span>
    </div>
    <div class="contact">
      4187 Marrow Creek Lane,<br>
      Suite K<br>
      Baton Rouge LA 70342<br>
      rowentallis@bellwickhomeservices.biz<br>
      www.bellwickhomeservice.biz
    </div>
    <div class="watermark"></div>
    <div class="footer">
      <div class="footer-rule"></div>
      <p class="footer-text">Commercial License # 53419 &nbsp;·&nbsp; Residential License # 21398</p>
      <div class="footer-band"></div>
    </div>
  </div>

  <!-- Letterhead option 2 -->
  <div class="sheet letterhead lh-two">
    <div class="brand">
      <span class="brand-mark"></span>
      <span class="brand-name">Bellwick Home Services</span>
    </div>
    <div class="watermark"></div>
    <div class="footer">
      <div class="footer-rule"></div>
      <p class="footer-text">4187 Marrow Creek Lane, Suite K, Baton Rouge LA 70342 &nbsp;·&nbsp; www.bellwickhomeservice.biz</p>
      <div class="footer-band"></div>
    </div>
  </div>

  <!-- Envelope backs -->
  <div class="sheet envelope-back">
    <svg width="270" height="245" viewBox="0 0 270 245" aria-hidden="true">
      <rect x="0" y="0" width="270" height="70" fill="var(--orange)"/>
      <rect x="0" y="78" width="270" height="165" fill="var(--paper)"/>
      <path d="M0 78 H270 V96 L150 150 Q135 156 120 150 L0 96 Z" fill="var(--flap)"/>
      <path d="M0 243 L120 180 Q135 174 150 180 L270 243" fill="none" stroke="#ddd" stroke-width="1"/>
    </svg>
  </div>

  <!-- Envelope front -->
  <div class="sheet envelope-front">
    <div class="brand">
      <span class="brand-mark"></span>
      <span class="brand-name">Bellwick Home Services</span>
    </div>
    <div class="return">
      4187 Marrow Creek Lane, Suite K<br>
      Baton Rouge LA 70342
    </div>
    <div class="watermark"></div>
    <div class="band"></div>
  </div>

</body>
</html>
```